Business Cards

I'd like help creating business cards with the full logo "Veltrona Capital Partners" on the back of the card (navy background with white writing), and abbreviated logo "VCP" on the front. Would like to list name, title, phone number, email, and website listed on front of card. Would like to keep very simple. Front font Arial or similar.

```html
<!DOCTYPE html>
<html lang="en">
<head>
<meta charset="utf-8">
<title>Veltrona Capital Partners – Business Cards</title>
<link href="https://fonts.googleapis.com/css2?family=Arimo:wght@400;700&display=swap" rel="stylesheet">
<style>
  :root {
    --navy: #021d8f;
    --navy-ink: #0a2a9c;
    --paper: #ffffff;
    --edge: #dfe3ee;
  }
  html, body {
    margin: 0;
    padding: 0;
    width: 1200px;
    height: 905px;
    overflow: hidden;
    background: var(--paper);
  }
  .sheet {
    position: relative;
    width: 1200px;
    height: 905px;
    font-family: "Arimo", Arial, sans-serif;
  }
  .card {
    position: absolute;
    top: 77px;
    width: 499px;
    height: 285px;
    box-sizing: border-box;
  }
  /* Back of card */
  .card-back {
    left: 83px;
    background: var(--navy);
    color: var(--paper);
  }
  .brand-name {
    position: absolute;
    left: 0;
    right: 0;
    top: 100px;
    text-align: center;
    font-weight: 700;
    line-height: 1;
  }
  .brand-name .primary {
    display: block;
    font-size: 44px;
    letter-spacing: 2px;
  }
  .brand-name .secondary {
    display: block;
    margin-top: 16px;
    font-size: 15px;
    letter-spacing: 8.6px;
  }
  /* Front of card */
  .card-front {
    left: 642px;
    background: var(--paper);
    border: 1px solid var(--edge);
    color: var(--navy-ink);
    overflow: hidden;
  }
  .band-right {
    position: absolute;
    top: 0;
    right: 0;
    width: 18px;
    height: 100%;
    background: var(--navy-ink);
  }
  .band-bottom {
    position: absolute;
    left: 0;
    bottom: 0;
    width: 100%;
    height: 15px;
    background: var(--navy-ink);
  }
  .initials {
    position: absolute;
    left: 38px;
    top: 20px;
    font-size: 40px;
    font-weight: 700;
    letter-spacing: 1px;
    line-height: 1;
  }
  .details {
    position: absolute;
    left: 184px;
    top: 23px;
    line-height: 1;
  }
  .employee-name {
    margin: 0;
    font-size: 21px;
    font-weight: 700;
  }
  .employee-title {
    margin: 5px 0 0;
    font-size: 15px;
  }
  .contact {
    margin: 0;
    padding: 0;
    list-style: none;
    font-size: 15px;
  }
  .contact li { position: absolute; left: 0; white-space: nowrap; }
  .contact .address { top: 71px; line-height: 19px; }
  .contact .email { top: 123px; }
  .contact .phone { top: 166px; }
  .contact .website { top: 206px; }
</style>
</head>
<body>
<main class="sheet">
  <section class="card card-back" aria-label="Back of business card">
    <h1 class="brand-name">
      <span class="primary">VELTRONA</span>
      <span class="secondary">CAPITAL PARTNERS</span>
    </h1>
  </section>

  <section class="card card-front" aria-label="Front of business card">
    <div class="initials">VCP</div>
    <div class="details">
      <h2 class="employee-name">EMPLOYEE NAME</h2>
      <p class="employee-title">TITLE</p>
      <ul class="contact">
        <li class="address">101 Address Ave<br>location, state zip</li>
        <li class="email">email@veltronamail.com</li>
        <li class="phone">888-888-8888</li>
        <li class="website">website</li>
      </ul>
    </div>
    <div class="band-right"></div>
    <div class="band-bottom"></div>
  </section>
</main>
</body>
</html>
```